Road Construction Company needs business cards

We would like a new business card designed for our business.

We're a road construction company based in Qld, Australia.

Can the business card please have the following information on it.

Name: Brent Malvoy
Position: General Manager
Phone: 0471 592 304
Email: Brent.malvoy@quendix.com.au
Address: 87 Harrowgate Ave, Pindarra, QLD, 4000
Website: www.quendix.com.au

Visually we'd like the card to be professional and simple.

Attached is our logo.

Our website is www.quendix.com.au

Target Market(s)

Men aged 25-60

Contact Information for Business Card

As listed in project description

Font styles to use
Serif

Requirements
Must have
• Large logo on back of card

```html
<!DOCTYPE html>
<html lang="en">
<head>
<meta charset="utf-8">
<title>Quendix Business Card</title>
<link rel="stylesheet" href="https://fonts.googleapis.com/css2?family=Montserrat:wght@400;500;800&family=Source+Serif+4:wght@300;400&display=swap">
<style>
  :root {
    --navy: #0353a0;
    --sky: #31a3d6;
    --paper: #ffffff;
    --backdrop: #e6f1f7;
    --sans: "Montserrat", Arial, sans-serif;
    --serif: "Source Serif 4", Georgia, serif;
  }
  * { margin: 0; padding: 0; box-sizing: border-box; }
  html, body { width: 1200px; height: 1200px; overflow: hidden; }
  body { background: var(--backdrop); position: relative; font-family: var(--sans); }

  .card {
    position: absolute;
    left: 359px;
    width: 482px;
    height: 295px;
    background: var(--paper);
    overflow: hidden;
  }
  .card-front { top: 234px; }
  .card-back { top: 626px; display: flex; align-items: center; justify-content: center; }

  .front-sweep { position: absolute; inset: 0; width: 482px; height: 295px; }

  .wordmark {
    font-family: var(--sans);
    font-weight: 800;
    color: var(--navy);
    letter-spacing: 0.02em;
    line-height: 1;
  }
  .card-front .wordmark { position: absolute; left: 219px; top: 28px; font-size: 38px; }
  .card-back .wordmark { font-size: 60px; margin-top: 6px; }

  .contact-list { position: absolute; left: 183px; top: 94px; list-style: none; }
  .contact-item {
    display: flex; align-items: center;
    height: 30px;
    color: var(--navy);
    font-size: 14px; font-weight: 500;
  }
  .contact-icon { width: 22px; height: 22px; margin-right: 12px; flex: none; }
  .contact-icon * { fill: none; stroke: var(--navy); stroke-width: 1.4; stroke-linecap: round; stroke-linejoin: round; }
  .address {
    position: absolute; left: 217px; top: 190px;
    color: var(--navy); font-size: 14px; font-weight: 500; line-height: 21px;
  }

  .holder { position: absolute; left: 16px; top: 218px; color: var(--paper); }
  .holder-name { font-family: var(--serif); font-weight: 300; font-size: 25px; line-height: 1; }
  .holder-role { font-family: var(--sans); font-weight: 400; font-size: 13px; margin-top: 2px; letter-spacing: 0.02em; }
</style>
</head>
<body>
  <section class="card card-front">
    <svg class="front-sweep" viewBox="0 0 482 295" aria-hidden="true">
      <path fill="var(--sky)" d="M0 0 H163 C118 70 116 160 172 222 C202 256 232 279 264 295 H0 Z"/>
      <path fill="var(--navy)" d="M0 0 H143 C110 60 112 152 166 216 C196 253 228 278 264 295 H0 Z"/>
    </svg>

    <div class="wordmark">QUENDIX</div>

    <ul class="contact-list">
      <li class="contact-item">
        <svg class="contact-icon" viewBox="0 0 22 22" aria-hidden="true">
          <path d="M5 4 L8 3.5 L9.5 7.5 L7.8 9 C8.6 11.5 10.2 13.3 12.6 14.4 L14 12.6 L18 14 L17.6 17 C12 17.8 5.2 11 5 4 Z"/>
          <path d="M12.5 3.5 A6 6 0 0 1 18.5 9.5"/>
          <path d="M12.5 6.5 A3 3 0 0 1 15.5 9.5"/>
        </svg>
        0471 592 304
      </li>
      <li class="contact-item">
        <svg class="contact-icon" viewBox="0 0 22 22" aria-hidden="true">
          <rect x="2" y="5" width="18" height="12"/>
          <path d="M2 5 L11 12 L20 5 M2 17 L8.5 10.5 M20 17 L13.5 10.5"/>
        </svg>
        Brent.malvoy@quendix.com.au
      </li>
      <li class="contact-item">
        <svg class="contact-icon" viewBox="0 0 22 22" aria-hidden="true">
          <circle cx="11" cy="11" r="8.5"/>
          <ellipse cx="11" cy="11" rx="3.8" ry="8.5"/>
          <path d="M2.5 11 H19.5 M4 6.5 H18 M4 15.5 H18 M11 2.5 V19.5"/>
        </svg>
        www.quendix.com.au
      </li>
    </ul>

    <p class="address">87 Harrowgate Ave, Pindarra,<br>QLD, 4000</p>

    <div class="holder">
      <p class="holder-name">Brent Malvoy</p>
      <p class="holder-role">General Manager</p>
    </div>
  </section>

  <section class="card card-back">
    <div class="wordmark">QUENDIX</div>
  </section>
</body>
</html>
```